Zuvo Decor

There is a sample provided with the arabic text of the business card. please copy paste the same text and the same Logo (The two triangles) Just try to incorproate the Brown background attached (you are free to change the colors) Id like the colors to be mainly shades of black and red.

```html
<!DOCTYPE html>
<html lang="ar">
<head>
<meta charset="utf-8">
<title>Zuvo Decor — Business Card</title>
<link rel="stylesheet" href="https://fonts.googleapis.com/css2?family=Tajawal:wght@400;500;700&family=Aref+Ruqaa:wght@400;700&display=swap">
<style>
  :root {
    --page-bg: #d9d9db;
    --card-black: #0b0b0c;
    --card-charcoal: #1c1c1e;
    --brand-red: #e5204d;
    --text-white: #f4f4f4;
    --text-soft: #dcdcdc;
  }
  * { box-sizing: border-box; margin: 0; padding: 0; }
  html, body { width: 1200px; height: 1200px; overflow: hidden; }
  body {
    background: var(--page-bg);
    font-family: "Tajawal", sans-serif;
    position: relative;
  }
  .card {
    position: absolute;
    left: 150px;
    width: 900px;
    height: 515px;
    border-radius: 26px;
    overflow: hidden;
    background: var(--card-black);
    border-bottom: 16px solid var(--brand-red);
    box-shadow: 0 18px 40px rgba(0,0,0,0.35);
  }
  .card--front { top: 70px; }
  .card--back { top: 620px; }
  .card__texture {
    position: absolute;
    inset: 0;
    background: radial-gradient(ellipse at 60% 45%, var(--card-charcoal) 0%, var(--card-black) 65%);
  }
  .brand {
    position: absolute;
    display: flex;
    align-items: center;
    gap: 12px;
    color: var(--text-white);
    font-family: "Tajawal", sans-serif;
    font-weight: 700;
    letter-spacing: 1px;
    direction: ltr;
    white-space: nowrap;
  }
  .brand__mark { background: var(--brand-red); display: block; }
  .card--front .brand { left: 150px; top: 222px; font-size: 46px; }
  .card--front .brand__mark { width: 22px; height: 22px; }
  .divider {
    position: absolute;
    left: 475px;
    top: 110px;
    width: 2px;
    height: 290px;
    background: var(--brand-red);
  }
  .profile {
    position: absolute;
    right: 60px;
    top: 105px;
    width: 350px;
    direction: rtl;
    text-align: right;
    color: var(--text-white);
  }
  .profile__name {
    font-family: "Aref Ruqaa", serif;
    font-size: 30px;
    line-height: 1.2;
    white-space: nowrap;
  }
  .profile__role {
    font-family: "Aref Ruqaa", serif;
    font-size: 20px;
    color: var(--text-soft);
    margin-bottom: 12px;
  }
  .profile__quals { list-style: none; font-size: 21px; line-height: 1.35; font-weight: 500; white-space: nowrap; }
  .profile__phone {
    margin-top: 14px;
    direction: ltr;
    display: flex;
    align-items: center;
    justify-content: flex-end;
    gap: 8px;
    font-size: 23px;
    font-weight: 700;
    letter-spacing: 0.5px;
  }
  .profile__phone svg { width: 20px; height: 20px; }
  .services {
    position: absolute;
    left: 90px;
    top: 70px;
    list-style: none;
    direction: rtl;
    color: var(--text-white);
    font-size: 31px;
    font-weight: 500;
    line-height: 1.38;
    white-space: nowrap;
  }
  .services li { display: flex; align-items: center; gap: 18px; }
  .services li::before {
    content: "";
    width: 12px;
    height: 12px;
    background: var(--brand-red);
    flex: none;
  }
  .card--back .brand { right: 70px; bottom: 55px; font-size: 38px; }
  .card--back .brand__mark { width: 18px; height: 18px; }
</style>
</head>
<body>

<section class="card card--front">
  <div class="card__texture" role="img" aria-label="Faint dark grid of squares and circles as background texture"></div>
  <div class="brand"><span class="brand__mark"></span><span>Zuvo Decor</span></div>
  <div class="divider"></div>
  <div class="profile">
    <p class="profile__name">المهندس / سامر يوسف الحداد</p>
    <p class="profile__role">أستاذ جامعي</p>
    <ul class="profile__quals">
      <li>ماجستير هندسة ديكور</li>
      <li>دبلوم عالي فن تشكيلي</li>
      <li>أكاديمية سيرال للفنون</li>
      <li>استشارات هندسية - فنية</li>
    </ul>
    <p class="profile__phone">
      <svg viewBox="0 0 24 24" aria-hidden="true"><path fill="#e5204d" d="M6.6 10.8a15.1 15.1 0 0 0 6.6 6.6l2.2-2.2a1 1 0 0 1 1-.25 11.4 11.4 0 0 0 3.6.57 1 1 0 0 1 1 1V20a1 1 0 0 1-1 1A17 17 0 0 1 3 4a1 1 0 0 1 1-1h3.5a1 1 0 0 1 1 1c0 1.25.2 2.46.57 3.6a1 1 0 0 1-.25 1z"/></svg>
      <span>35550142 / 66550187</span>
    </p>
  </div>
</section>

<section class="card card--back">
  <div class="card__texture" role="img" aria-label="Faint dark grid of squares and circles as background texture"></div>
  <ul class="services">
    <li>ماجستير هندسة ديكور</li>
    <li>دبلوم عالي فن تشكيلي</li>
    <li>أكاديمية سيرال للفنون</li>
    <li>استشارات هندسية - فنية</li>
    <li>ماجستير هندسة ديكور</li>
    <li>دبلوم عالي فن تشكيلي</li>
    <li>أكاديمية سيرال للفنون</li>
    <li>استشارات هندسية - فنية</li>
  </ul>
  <div class="brand"><span class="brand__mark"></span><span>Zuvo Decor</span></div>
</section>

</body>
</html>
```